Law Enforcement Consulting Group Website

We are working with a Law Enforcement Consulting Group called Penwick Group. They help law enforcement agencies develop policies, training tools, solve problems, etc...

Some sites to use for content/competitors:
https://harborlineadvisors.example
https://vantorqglobal.example/military-law/law-enforcement-consulting-services/
https://harborlineadvisors.example/services/police-services/

Consulting websites for inspiration ( we found these sites to fit better with the brand, and identity of the client:

https://drift.example
https://truevoxa.example
https://www.dorentvale.example
https://lorabettcress.example
https://sevrinokadu.example
https://themes.pelbrixstudio.example/be/consultant2/
https://themes.pelbrixstudio.example/be/consultant/

Thank you for taking the time to consider designing a website for us. We are web developers based in Stockton, CA, USA. Most of our projects go through the same process. Understanding this process may help you win a project with us. We custom-code all of our websites in-house. We don’t have any requirements as to what tools you use for your design, but we prefer Figma files. For any design that we label as four-stars, we send it to the client for review. The client picks the final design they want us to use. Once we complete this process, we will continue to show additional clients all the four-star sites and purchase them later. Your designs will have multiple chances to sell. For better chances of success, we ask that you follow these guidelines.

IMAGES:
If you use any images or icons in the design, we ask that you have a link to the asset so we can purchase the image/icon. Most of the designs we submit do not have the customer’s images on them unless they have some great images. Be creative; show us the feeling you are trying to portray with your image choices. Use any royalty-free site you choose. We subscribe to Adobe and mainly use their images, but we can purchase images outside of Adobe.
PLEASE NOTE: we will not submit designs to clients with watermarks on the images.

FONTS:
We ask that you identify the fonts used in the design. This can be done in a message if you want. We typically use Google Fonts and Adobe Fonts.

CONTENT:
We're always open to different content and ideas. We often submit designs with stock images so the client can see our vision. We typically take pictures after the website launch to use their images with our vision. Lorem Ipsum is fine for paragraphs, but we ask that you write the headers in correct English. We want to be able to show the vision and identify the sections of the website.

INSPIRATION:
We typically add a couple of links in the brief of websites we like to help you get started in your design.

REVISIONS:
We do not often ask for revisions of the designs unless we see something in the design that may not appeal to the client. If there are slight changes that we want to make, we do that in the development process.

FEEDBACK:
We rarely give feedback on designs during the design process. We are working on many website projects and do not have the time to provide feedback. We usually respond if your request is well thought out and asks specific questions, but a note asking “feedback, please” usually goes unanswered.

```html
<!DOCTYPE html>
<html lang="en">
<head>
<meta charset="utf-8">
<title>Penwick Group — Law Enforcement Consulting</title>
<link href="https://fonts.googleapis.com/css2?family=Rubik:wght@500;600;700;800&family=Montserrat:wght@400;500;600;700&display=swap" rel="stylesheet">
<style>
:root{
  --red:#e0361f;
  --red-dark:#c42a17;
  --ink:#1b1b1b;
  --text:#555;
  --grey-band:#f3f3f3;
  --gold:#f2a33a;
  --footer:#222225;
  --white:#fff;
  --head:"Rubik",sans-serif;
  --body:"Montserrat",sans-serif;
}
*{box-sizing:border-box;margin:0;padding:0}
html,body{width:1200px;height:4054px;overflow:hidden}
body{position:relative;font-family:var(--body);color:var(--ink);background:var(--white)}
.abs{position:absolute}
.hex{clip-path:polygon(50% 0,100% 25%,100% 75%,50% 100%,0 75%,0 25%)}
.btn{position:absolute;display:flex;align-items:center;background:var(--red);color:#fff;font-family:var(--body);font-weight:700;font-size:15px;height:40px;padding-left:18px;overflow:hidden}
.btn .arrow{position:absolute;right:0;top:0;width:30px;height:100%;background:#111;clip-path:polygon(35% 0,100% 0,100% 100%,0 100%);display:flex;align-items:center;justify-content:center}
.btn .arrow svg{margin-left:8px}
.btn.white{background:#fff;color:var(--red)}
.label{font-family:var(--body);font-weight:500;font-size:14px;color:var(--red);letter-spacing:.3px}
.h2{font-family:var(--head);font-weight:700;font-size:34px;letter-spacing:-.3px;text-transform:uppercase}
.center{left:0;width:1200px;text-align:center}

/* nav */
.topbar{left:0;top:0;width:1200px;height:4px;background:var(--red)}
.nav{left:0;top:4px;width:1200px;height:76px;background:#fff}
.brand{display:flex;align-items:center;gap:10px;left:143px;top:18px}
.brand .mark{width:40px;height:40px;border:4px solid var(--red);border-radius:50%}
.brand span{font-family:var(--head);font-weight:700;font-size:22px;color:var(--red)}
.menu{left:412px;top:31px;display:flex;gap:0;font-size:15px}
.menu a{position:absolute;white-space:nowrap;color:#222;text-decoration:none}

/* hero */
.hero{left:0;top:80px;width:1200px;height:602px;background:linear-gradient(100deg,#1a2430 0%,#2b3a4a 45%,#51463d 70%,#2a2a2e 100%)}
.hero-title{left:143px;top:240px;font-family:var(--head);font-weight:700;font-size:52px;color:#fff}
.hero-text{left:143px;top:318px;width:430px;font-size:16px;line-height:29px;color:#fff}

/* stats */
.stat{display:flex;align-items:center;gap:20px}
.stat .num{font-family:var(--head);font-weight:700;font-size:38px;color:var(--gold);line-height:1}
.stat .cap{font-size:13px;font-weight:500;color:#333;margin-top:10px}
.divider{width:1px;height:80px;background:#ddd;top:725px}

/* about */
.about-band{left:0;top:875px;width:716px;height:485px;background:var(--grey-band);clip-path:polygon(0 0,505px 0,716px 450px,700px 485px,0 485px)}
.sub{font-size:16px;line-height:28px;color:#222}
.para{font-size:13.5px;line-height:24px;color:var(--text)}

/* services */
.services{left:0;top:1500px;width:1200px;height:633px;background:linear-gradient(120deg,#e33a22,#d22f1b 60%,#e2452b)}
.svc{position:absolute;width:168px;height:192px;background:#fff;display:flex;flex-direction:column;align-items:center;justify-content:center;text-align:center;font-size:14px;color:#222;gap:10px;line-height:20px}
.svc svg{stroke:var(--ink);fill:none;stroke-width:2}
.svc svg .r{stroke:var(--red)}

/* projects */
.proj-bg{left:465px;top:2190px;width:735px;height:480px;background:var(--grey-band);clip-path:polygon(180px 0,100% 0,100% 100%,0 100%)}
.photo{border-radius:8px}

/* testimonials */
.avatar{position:absolute;border:3px solid #fff;box-shadow:0 3px 10px rgba(0,0,0,.15)}
.dots{left:549px;top:3164px;display:flex;gap:8px}
.dots i{display:block;width:16px;height:5px;background:#ddd}
.dots i:first-child{width:28px;background:var(--red)}

/* contact */
.contact{left:0;top:3247px;width:1200px;height:509px;background:linear-gradient(120deg,#e0361f,#d5301c)}
.field{position:absolute;border-bottom:1px solid rgba(255,255,255,.7);color:#fff;font-size:11px;padding-bottom:12px;display:flex;align-items:center;gap:5px}

/* footer */
.footer{left:0;top:3756px;width:1200px;height:298px;background:var(--footer)}
.fh{font-size:16px;font-weight:600;color:#fff;letter-spacing:.3px}
.flinks{display:flex;flex-direction:column;gap:6px;font-size:13px;color:#ddd}
.social{width:26px;height:26px;border-radius:50%;background:#fff}
</style>
</head>
<body>

<!-- navigation -->
<div class="abs topbar"></div>
<header class="abs nav"></header>
<div class="abs brand"><div class="mark"></div><span>Penwick Group</span></div>
<nav class="abs menu">
  <a style="left:0;color:var(--red)">Home</a>
  <a style="left:84px">About Us</a>
  <a style="left:194px">Services</a>
  <a style="left:293px">Projects</a>
  <a style="left:390px">Contact</a>
</nav>
<div class="btn" style="left:896px;top:25px;width:159px;height:33px;font-size:14px;padding-left:12px">Schedule a Call<span class="arrow"><svg width="8" height="10" viewBox="0 0 8 10"><path d="M2 1l4 4-4 4" stroke="#fff" stroke-width="1.6" fill="none"/></svg></span></div>

<!-- hero -->
<section class="abs hero" role="img" aria-label="Photo of a smiling consultant in a suit holding a tablet in front of an office building"></section>
<h1 class="abs hero-title">PENWICK GROUP</h1>
<p class="abs hero-text">Lorem ipsum dolor sit amet, consectetur adipiscing elit,sed do eiusmod tempor incididunt</p>
<a class="btn" style="left:143px;top:401px;width:160px;height:46px;font-size:16px">Get Started<span class="arrow"><svg width="8" height="10" viewBox="0 0 8 10"><path d="M2 1l4 4-4 4" stroke="#fff" stroke-width="1.6" fill="none"/></svg></span></a>

<!-- stats -->
<div class="abs stat" style="left:147px;top:726px">
  <svg width="80" height="60" viewBox="0 0 80 60" fill="none" stroke="var(--red)" stroke-width="2.5"><path d="M4 18l14-6 14 8 10-4 14 6 18-6M8 26l18 18 8 4 10-4 16-14M30 34l10 10M36 28l12 10"/></svg>
  <div><div class="num">+2k</div><div class="cap">HAPPY CLIENTS</div></div>
</div>
<div class="abs divider" style="left:425px"></div>
<div class="abs stat" style="left:492px;top:726px">
  <svg width="72" height="72" viewBox="0 0 72 72" fill="none" stroke="var(--red)" stroke-width="2.5"><circle cx="40" cy="28" r="14"/><circle cx="40" cy="28" r="6"/><path d="M20 40c-8 4-10 16-2 22h14v-10M26 10l4 4M54 10l-4 4M40 6v6"/></svg>
  <div><div class="num">+2500</div><div class="cap">COMPLETED PROJECTS</div></div>
</div>
<div class="abs divider" style="left:797px"></div>
<div class="abs stat" style="left:860px;top:726px">
  <svg width="66" height="72" viewBox="0 0 66 72" fill="none" stroke="var(--red)" stroke-width="2.5"><path d="M33 6l4 8 8 1-6 6 2 8-8-4-8 4 2-8-6-6 8-1zM10 14l2 4 4 1-3 3 1 4-4-2-4 2 1-4-3-3 4-1zM56 14l2 4 4 1-3 3 1 4-4-2-4 2 1-4-3-3 4-1zM6 36l6 20 14 10M60 36l-6 20-14 10M20 44l10 14M46 44l-10 14"/></svg>
  <div><div class="num">100%</div><div class="cap">SUCCESS</div></div>
</div>

<!-- about -->
<div class="abs about-band"></div>
<div class="abs label center" style="top:896px">ABOUT US</div>
<h2 class="abs h2 center" style="top:925px">A Trusted Resource for Law Enforcement</h2>
<p class="abs sub" style="left:250px;width:700px;top:978px;text-align:center">Duis aute irure dolor in reprehenderit in voluptate velit esse cillum dolore eu fugiat nulla pariatur. Excepteur sint occaecat cupidatat non proident.</p>
<p class="abs para" style="left:143px;top:1074px;width:415px">Lorem ipsum dolor sit amet, consectetur adipiscing elit, sed do eiusmod tempor incididunt ut labore et dolore magna aliqua. Ut enim ad minim veniam, quis nostrud exercitation ullamco laboris nisi ut aliquip ex ea commodo consequat. Duis aute irure dolor in reprehenderit in voluptate velit esse cillum dolore eu fugiat nulla pariatur.</p>
<a class="btn" style="left:143px;top:1253px;width:140px">Learn More<span class="arrow"><svg width="8" height="10" viewBox="0 0 8 10"><path d="M2 1l4 4-4 4" stroke="#fff" stroke-width="1.6" fill="none"/></svg></span></a>
<div class="abs hex" style="left:754px;top:1053px;width:354px;height:408px;background:linear-gradient(160deg,#8a8f96,#3a4656 55%,#20242c)" role="img" aria-label="Portrait of a confident consultant with arms crossed outside an office building"></div>
<div class="abs hex" style="left:963px;top:1292px;width:140px;height:155px;background:var(--red)"></div>
<div class="abs hex" style="left:972px;top:1302px;width:122px;height:135px;background:#fff"></div>

<!-- services -->
<section class="abs services" role="img" aria-label="Red-tinted photo of uniformed police officers and first responders"></section>
<div class="abs label center" style="top:1556px;color:#fff;font-size:13px">WHAT WE DO</div>
<h2 class="abs h2 center" style="top:1582px;color:#fff">Penwick Group Services</h2>
<p class="abs sub" style="left:250px;width:700px;top:1636px;text-align:center;color:#fff">Duis aute irure dolor in reprehenderit in voluptate velit esse cillum dolore eu fugiat nulla pariatur. Excepteur sint occaecat cupidatat non proident.</p>

<div class="svc hex" style="left:136px;top:1724px"><svg width="56" height="52" viewBox="0 0 56 52"><path d="M10 40h36M14 40v-8a14 14 0 0128 0v8"/><path class="r" d="M28 16v10M24 22h8"/></svg>Fire &amp; EMS</div>
<div class="svc hex" style="left:321px;top:1724px"><svg width="56" height="52" viewBox="0 0 56 52"><circle cx="28" cy="26" r="16"/><circle class="r" cx="28" cy="24" r="5"/><path class="r" d="M20 36c2-6 14-6 16 0"/></svg>Administrative<br>Services</div>
<div class="svc hex" style="left:512px;top:1718px;width:176px;height:202px"><svg width="56" height="52" viewBox="0 0 56 52"><path d="M16 46V14h16v32M32 24h10v22M10 46h38M20 20h8M20 28h8M20 36h8"/></svg>Clerk's Office<svg width="20" height="20" viewBox="0 0 20 20"><circle class="r" cx="10" cy="10" r="8"/><path class="r" d="M7 10h6M10 7l3 3-3 3"/></svg></div>
<div class="svc hex" style="left:713px;top:1724px"><svg width="56" height="52" viewBox="0 0 56 52"><circle class="r" cx="30" cy="14" r="9"/><path d="M6 34l12-4h14l-10 6M6 44l16-2 22-14"/></svg>Financial</div>
<div class="svc hex" style="left:898px;top:1724px"><svg width="56" height="52" viewBox="0 0 56 52"><circle class="r" cx="28" cy="16" r="6"/><circle class="r" cx="20" cy="10" r="3"/><circle class="r" cx="36" cy="10" r="3"/><path d="M8 20l6 18 10 8M48 20l-6 18-10 8"/></svg>Animal Care</div>

<div class="svc hex" style="left:241px;top:1880px"><svg width="56" height="52" viewBox="0 0 56 52"><circle class="r" cx="18" cy="10" r="4"/><circle class="r" cx="28" cy="8" r="4"/><circle class="r" cx="38" cy="10" r="4"/><path d="M6 28l12-6 10 6 10-6 12 6M12 34l10 10h12l10-10"/></svg>Public Works</div>
<div class="svc hex" style="left:425px;top:1880px"><svg width="56" height="52" viewBox="0 0 56 52"><circle class="r" cx="28" cy="26" r="8"/><circle cx="10" cy="18" r="4"/><circle cx="46" cy="18" r="4"/><circle cx="28" cy="6" r="3"/><path d="M2 36c2-6 14-6 16 0M38 36c2-6 14-6 16 0"/></svg>Human Resources</div>
<div class="svc hex" style="left:610px;top:1880px"><svg width="56" height="52" viewBox="0 0 56 52"><path class="r" d="M6 22L28 4l22 18"/><path d="M12 20v26h32V20"/><circle cx="28" cy="28" r="5"/><path d="M20 44c1-6 15-6 16 0"/></svg>Homelessness &amp;<br>Housing</div>
<div class="svc hex" style="left:795px;top:1880px"><svg width="56" height="52" viewBox="0 0 56 52"><path d="M28 4l18 6v14c0 12-8 20-18 24C18 44 10 36 10 24V10z"/><path class="r" d="M28 16l3 6 6 1-4 4 1 6-6-3-6 3 1-6-4-4 6-1z"/></svg>Police Services</div>

<!-- projects -->
<div class="abs proj-bg"></div>
<div class="abs label" style="left:143px;top:2264px">WORKS</div>
<h2 class="abs h2" style="left:143px;top:2290px">Our Projects</h2>
<p class="abs sub" style="left:143px;top:2345px;width:420px">Duis aute irure dolor in reprehenderit in voluptate velit esse cillum dolore eu pariatur.</p>
<p class="abs para" style="left:143px;top:2413px;width:415px">Lorem ipsum dolor sit amet, consectetur adipiscing elit, sed do eiusmod tempor incididunt ut labore et dolore magna aliqua. Ut enim ad minim veniam, quis nostrud exercitation ullamco laboris nisi ut aliquip ex ea commodo</p>
<a class="btn" style="left:143px;top:2544px;width:140px">View More<span class="arrow"><svg width="8" height="10" viewBox="0 0 8 10"><path d="M2 1l4 4-4 4" stroke="#fff" stroke-width="1.6" fill="none"/></svg></span></a>
<div class="abs photo" style="left:626px;top:2238px;width:406px;height:377px;background:linear-gradient(135deg,#c9bfae,#6d6a66 55%,#2c2f38)" role="img" aria-label="Photo of three consultants collaborating around a laptop"></div>
<div class="abs photo" style="left:1049px;top:2238px;width:170px;height:377px;background:linear-gradient(160deg,#3a4252,#1b1f29)" role="img" aria-label="Photo of police officers in tactical gear"></div>

<!-- testimonials -->
<div class="abs label center" style="top:2746px">CLIENT FEEDBACK</div>
<h2 class="abs h2 center" style="top:2772px">What Our Clients Says</h2>
<div class="abs hex" style="left:544px;top:2843px;width:112px;height:124px;background:var(--red)"></div>
<div class="abs hex" style="left:550px;top:2850px;width:100px;height:110px;background:linear-gradient(160deg,#5f6f86,#2d3a52)" role="img" aria-label="Client portrait"></div>
<div class="avatar hex" style="left:230px;top:2890px;width:56px;height:62px;background:linear-gradient(160deg,#9aa0a8,#4b5563)" role="img" aria-label="Client portrait"></div>
<div class="avatar hex" style="left:990px;top:2855px;width:62px;height:70px;background:linear-gradient(160deg,#8893a5,#3e4a60)" role="img" aria-label="Client portrait"></div>
<div class="avatar hex" style="left:820px;top:2905px;width:36px;height:40px;background:linear-gradient(160deg,#b7aca2,#5d5552)" role="img" aria-label="Client portrait"></div>
<div class="avatar hex" style="left:145px;top:3026px;width:38px;height:42px;background:linear-gradient(160deg,#7b818c,#2e3440)" role="img" aria-label="Client portrait"></div>
<div class="avatar hex" style="left:355px;top:3085px;width:40px;height:44px;background:linear-gradient(160deg,#a08b80,#3f3431)" role="img" aria-label="Client portrait"></div>
<div class="avatar hex" style="left:825px;top:3076px;width:54px;height:60px;background:linear-gradient(160deg,#a59a90,#403836)" role="img" aria-label="Client portrait"></div>
<p class="abs para center" style="left:285px;width:630px;top:2982px;font-size:14px;line-height:28px">Lorem ipsum dolor sit amet, consectetur adipiscing elit, sed do eiusmod tempor incididunt ut labore et dolore magna aliqua. Ut enim ad minim veniam, quis nostrud exercitation ullamco laboris nisi ut aliquip ex ea commodo consequat.</p>
<div class="abs center" style="top:3088px;font-size:17px;font-weight:600;color:#222">Dorian Kessler</div>
<div class="abs center" style="top:3116px;font-size:12px;color:var(--red)">Lorem Ipsum</div>
<div class="abs dots"><i></i><i></i><i></i><i></i></div>

<!-- contact -->
<section class="abs contact" role="img" aria-label="Red-tinted backdrop of a city skyline"></section>
<div class="abs" style="left:0;top:3105px;width:252px;height:580px;background:#fff;clip-path:polygon(0 0,100% 28%,100% 96%,0 100%)"></div>
<div class="abs" style="left:0;top:3110px;width:246px;height:566px;background:linear-gradient(150deg,#9ba3ab,#56595e 50%,#2f3035);clip-path:polygon(0 0,100% 28%,100% 96%,0 100%)" role="img" aria-label="Photo of a thoughtful consultant with glasses working on a laptop"></div>
<div class="abs label" style="left:493px;top:3298px;color:#fff">SEND A MESSAGE</div>
<h2 class="abs h2" style="left:493px;top:3324px;color:#fff">How Can We Serve You?</h2>
<div class="field" style="left:497px;top:3400px;width:260px">&#9906; First Name</div>
<div class="field" style="left:793px;top:3400px;width:260px">&#9906; Last Name</div>
<div class="field" style="left:497px;top:3470px;width:260px">&#9993; Email Address</div>
<div class="field" style="left:793px;top:3470px;width:260px">&#9990; Phone Number</div>
<div class="field" style="left:497px;top:3540px;width:556px;height:70px;align-items:flex-start">&#9679; Message</div>
<a class="btn white" style="left:497px;top:3680px;width:140px">Submit Now<span class="arrow"><svg width="8" height="10" viewBox="0 0 8 10"><path d="M2 1l4 4-4 4" stroke="#fff" stroke-width="1.6" fill="none"/></svg></span></a>

<!-- footer -->
<footer class="abs footer"></footer>
<div class="abs brand" style="top:3842px"><div class="mark" style="width:46px;height:46px"></div><span style="color:#fff;font-size:24px">Penwick Group</span></div>
<div class="abs fh" style="left:402px;top:3803px">QUICK LINKS</div>
<div class="abs flinks" style="left:402px;top:3838px"><span>Home</span><span>About Us</span><span>Services</span><span>Projects</span><span>Contact</span><span>Schedule A Call</span></div>
<div class="abs fh" style="left:585px;top:3803px">OTHER LINKS</div>
<div class="abs flinks" style="left:585px;top:3838px"><span>Terms of Services</span><span>Terms &amp; Condition</span><span>Privacy Policy</span></div>
<div class="abs social" style="left:585px;top:3925px;background:var(--red)"></div>
<div class="abs social" style="left:622px;top:3925px"></div>
<div class="abs social" style="left:659px;top:3925px"></div>
<div class="abs fh" style="left:794px;top:3803px">SUBSCRIBE FOR UPDATES</div>
<div class="abs" style="left:794px;top:3823px;width:259px;height:40px;background:#fff;border-radius:3px;font-size:11px;color:#888;padding:13px 16px">Email Address</div>
<svg class="abs" style="left:1029px;top:3836px" width="14" height="14" viewBox="0 0 14 14"><path d="M1 7l12-6-4 12-2-5z" fill="none" stroke="var(--red)" stroke-width="1.4"/></svg>
<div class="abs" style="left:794px;top:3898px;font-size:14px;color:#fff"><span style="color:var(--red)">&#9993;</span>&nbsp; Email :&nbsp; info@penwickgroup.example</div>
<div class="abs" style="left:794px;top:3926px;font-size:14px;color:#fff"><span style="color:var(--red)">&#9990;</span>&nbsp; Phone :&nbsp; 1+888-555-0142</div>
<div class="abs" style="left:1071px;top:3985px;width:34px;height:34px;border-radius:50%;background:var(--red);display:flex;align-items:center;justify-content:center"><svg width="12" height="8" viewBox="0 0 12 8"><path d="M1 7l5-5 5 5" stroke="#fff" stroke-width="1.8" fill="none"/></svg></div>
<div class="abs center" style="top:4015px;font-size:12px;color:#ddd">2025 Copyright - Penwick Group | All Rights Reserved</div>

</body>
</html>
```